HARLOWE CONSERVATORY SAXOPHONE SENIOR RECITAL

I need a poster design for my senior saxophone recital. The title of it is "Quill: a Voyage beneath the Edge of Tone". My concept is completely contrasting to the idea of a typical university recital. I'm so put off by the idea of "clap..clap..{play some music}..clap..clap..repeat". My recital is all based off of sound. The music I selected is all very modern (i.e Brem Ostrakel 'Warm from the First Pour' for Saxophone and Coffee Machine). I've included the Chatterbox link so you can see the picture I have in the background. I like the idea of minimal black and white photography. Also, I would like the time / date / location / etc. all included on it. Let your imaginations run wild! It's art for an artist!
https://www.chatterbox-example.net/events/412093857716230/
Target Market(s)
University Students around the Harlowe Conservatory and locals around the art district of South Beach, FL.
Industry/Entity Type
University
Look and feel

```html
<!DOCTYPE html>
<html lang="en">
<head>
<meta charset="utf-8">
<title>Quill: a Voyage beneath the Edge of Tone — Senior Saxophone Recital</title>
<link rel="stylesheet" href="https://fonts.googleapis.com/css2?family=Archivo+Black&family=Archivo:wght@300;700&display=swap">
<style>
  :root {
    --sky-deep: #2b323c;
    --sky-mid: #5a6572;
    --cloud: #c9cdd0;
    --cloud-bright: #e4e6e7;
    --ground: #1e242b;
    --teal: #1fa9a2;
    --teal-edge: #0c3f3c;
    --white: #ffffff;
    --ink-edge: #1b1f24;
  }
  html, body {
    margin: 0;
    padding: 0;
    width: 1200px;
    height: 845px;
    overflow: hidden;
    background: var(--ground);
  }
  .poster {
    position: relative;
    width: 1200px;
    height: 845px;
    overflow: hidden;
  }
  .poster__photo {
    position: absolute;
    inset: 0;
    background:
      radial-gradient(ellipse 38% 16% at 42% 28%, var(--cloud-bright) 0%, rgba(228,230,231,0) 100%),
      radial-gradient(ellipse 30% 14% at 18% 30%, var(--cloud) 0%, rgba(201,205,208,0) 100%),
      radial-gradient(ellipse 26% 14% at 80% 36%, var(--cloud) 0%, rgba(201,205,208,0) 100%),
      radial-gradient(ellipse 60% 24% at 50% 32%, rgba(160,168,175,0.8) 0%, rgba(160,168,175,0) 100%),
      linear-gradient(180deg, var(--sky-deep) 0%, var(--sky-mid) 30%, #6a7480 50%, #3f4852 70%, var(--ground) 100%);
  }
  .poster__info {
    position: absolute;
    right: 55px;
    top: 494px;
    text-align: right;
    color: var(--white);
  }
  .poster__title {
    margin: 0;
    font-family: "Archivo Black", sans-serif;
    font-size: 40px;
    line-height: 1;
    letter-spacing: -0.5px;
    color: var(--teal);
    -webkit-text-stroke: 1.5px var(--teal-edge);
    text-transform: uppercase;
    white-space: nowrap;
  }
  .poster__performer {
    margin: 12px 0 0;
    font-family: "Archivo Black", sans-serif;
    font-size: 25px;
    line-height: 1;
    letter-spacing: -0.3px;
    -webkit-text-stroke: 1px var(--ink-edge);
    text-transform: uppercase;
    white-space: nowrap;
  }
  .poster__institution {
    margin: 28px 0 0;
    font-family: "Archivo", sans-serif;
    font-weight: 300;
    font-size: 27px;
    line-height: 1;
    letter-spacing: 0.5px;
    white-space: nowrap;
  }
  .poster__venue,
  .poster__date {
    margin: 14px 0 0;
    font-family: "Archivo", sans-serif;
    font-weight: 700;
    font-size: 23px;
    line-height: 1;
    -webkit-text-stroke: 0.8px var(--ink-edge);
    white-space: nowrap;
  }
  .poster__date { margin-top: 17px; }
</style>
</head>
<body>
  <main class="poster">
    <div class="poster__photo" role="img" aria-label="Black and white halftone photograph of a cloudy sky over a beach, with small silhouetted figures standing at the lower right"></div>
    <section class="poster__info">
      <h1 class="poster__title">Quill: a Voyage beneath the Edge of Tone</h1>
      <p class="poster__performer">Dario Velloquin Senior Saxophone Recital</p>
      <p class="poster__institution">HARLOWE CONSERVATORY</p>
      <p class="poster__venue">Marsh Linden Recital Hall</p>
      <p class="poster__date">8 December 2013, 14.00</p>
    </section>
  </main>
</body>
</html>
```